Business Card Design for Varnok Facility Services

We are looking for a Business Card Design for the Company "Varnok Facility Services."
Front side:
- Company Logo (small)
- Company Name, address, pohone, website and personal data.
- white background, for text e.g. company colors (blue or green like in the logo)
Please use following data:
Company data:
Varnok Facility Services Tulbrecht
Kirchmattweg 12
6331 Cham
www.varnok-fs.ch
Person data:
Ruben Tulbrecht
Geschäftsführer
+41 76 519 84 60
info@varnok-fs.ch
Back side:
could be colored in blue or green
please use a big logo sing and some smaller icons to say what is all beeing offered in facility services, like cleaning, maintenance cleaning
industrial cleaning, caretaking, gardening, disposal. There is no need for everyone of the icons if there are similar or an icon is standing for more of them.
Cleaning Service
colors to use:
blue: HEX 246BB0
green: HEX 52B33E

```html
<!DOCTYPE html>
<html lang="de">
<head>
<meta charset="utf-8">
<title>Varnok Facility Services – Visitenkarte</title>
<link rel="stylesheet" href="https://fonts.googleapis.com/css2?family=Arimo:wght@400;700&family=Michroma&display=swap">
<style>
  :root {
    --blue: #246bb0;
    --blue-deep: #0a72b0;
    --green: #52b33e;
    --green-band: #4dad3c;
    --paper: #ffffff;
    --canvas: #ffffff;
    --frame: #d0d0d0;
    --icon-tone: #5a6a5a;
  }
  html, body {
    margin: 0;
    padding: 0;
    width: 1200px;
    height: 1200px;
    overflow: hidden;
    background: var(--canvas);
  }
  .canvas {
    position: relative;
    width: 1200px;
    height: 1200px;
    box-sizing: border-box;
    border: 1px solid var(--frame);
    font-family: "Arimo", Arial, sans-serif;
  }
  .card {
    position: absolute;
    left: 312px;
    width: 575px;
    height: 338px;
    background: var(--paper);
    box-shadow: 0 0 22px rgba(0,0,0,0.12);
    overflow: hidden;
  }
  .card--front { top: 194px; }
  .card--back { top: 668px; }

  /* Front */
  .front-brand {
    position: absolute;
    left: 36px;
    top: 36px;
    display: flex;
    align-items: center;
    gap: 8px;
  }
  .front-brand__square {
    width: 18px;
    height: 18px;
    background: var(--green);
  }
  .front-brand__name {
    font-weight: 700;
    font-size: 19px;
    color: var(--blue);
    letter-spacing: 0.5px;
  }
  .contact {
    position: absolute;
    right: 30px;
    top: 33px;
    text-align: right;
    color: var(--blue-deep);
    font-size: 15.5px;
    line-height: 21.5px;
  }
  .contact__name {
    color: var(--green);
    font-weight: 700;
    font-size: 17.5px;
    line-height: 22px;
  }
  .rule {
    position: absolute;
    left: 0;
    width: 100%;
    height: 2.5px;
    background: var(--blue-deep);
  }
  .rule--top { top: 222px; }
  .rule--bottom { top: 266px; }
  .company-band {
    position: absolute;
    left: 0;
    top: 228px;
    width: 100%;
    height: 35px;
  }
  .address {
    position: absolute;
    left: 0;
    top: 277px;
    width: 100%;
    text-align: center;
    color: var(--blue-deep);
    font-size: 16px;
    line-height: 20px;
  }

  /* Back */
  .back-band {
    position: absolute;
    left: 0;
    width: 100%;
  }
  .back-band--top { top: 0; height: 36px; background: var(--green-band); }
  .back-band--bottom { bottom: 0; height: 37px; background: var(--blue-deep); }
  .back-brand {
    position: absolute;
    left: 0;
    top: 72px;
    width: 100%;
    text-align: center;
    color: var(--blue);
    font-weight: 700;
  }
  .back-brand__circle {
    width: 70px;
    height: 70px;
    margin: 0 auto 14px;
    border-radius: 50%;
    background: var(--green);
  }
  .back-brand__name {
    font-size: 42px;
    line-height: 42px;
    letter-spacing: 3px;
  }
  .back-brand__sub {
    font-size: 19px;
    line-height: 24px;
    letter-spacing: 4px;
    margin-top: 4px;
  }
  .service-row {
    position: absolute;
    left: 134px;
    top: 250px;
    display: flex;
    gap: 29px;
  }
  .service-tile {
    width: 83px;
    height: 60px;
    box-sizing: border-box;
    border: 1px solid var(--green);
    border-radius: 8px;
    background: var(--paper);
    display: flex;
    align-items: center;
    justify-content: center;
  }
  .service-tile__art {
    width: 48px;
    height: 42px;
    border-radius: 4px;
    background: linear-gradient(135deg, var(--icon-tone), #2b2b2b);
    opacity: 0.85;
  }
</style>
</head>
<body>
<div class="canvas">

  <section class="card card--front" aria-label="Vorderseite">
    <div class="front-brand">
      <span class="front-brand__square"></span>
      <span class="front-brand__name">Varnok Facility Services</span>
    </div>

    <div class="contact">
      <div class="contact__name">Ruben Tulbrecht</div>
      <div>Geschäftsführer</div>
      <div>+41 76 519 84 60</div>
      <div>info@varnok-fs.ch</div>
    </div>

    <div class="rule rule--top"></div>
    <svg class="company-band" viewBox="0 0 575 35" preserveAspectRatio="none">
      <rect width="575" height="35" fill="var(--green-band)"/>
      <text x="287.5" y="24.5" text-anchor="middle" textLength="530" lengthAdjust="spacingAndGlyphs"
            font-family="Michroma, sans-serif" font-size="19" fill="#ffffff">VARNOK FACILITY SERVICES TULBRECHT</text>
    </svg>
    <div class="rule rule--bottom"></div>

    <div class="address">
      <div>Kirchmattweg 12, 6331 Cham.</div>
      <div>www.varnok-fs.ch</div>
    </div>
  </section>

  <section class="card card--back" aria-label="Rückseite">
    <div class="back-band back-band--top"></div>

    <div class="back-brand">
      <div class="back-brand__circle"></div>
      <div class="back-brand__name">VARNOK</div>
      <div class="back-brand__sub">FACILITY SERVICES</div>
    </div>

    <div class="back-band back-band--bottom"></div>

    <div class="service-row">
      <div class="service-tile"><div class="service-tile__art" role="img" aria-label="Piktogramm: Reinigungskraft mit Industriesauger und Wischmopp"></div></div>
      <div class="service-tile"><div class="service-tile__art" role="img" aria-label="Piktogramm: Gärtner kniend bei Pflanzen"></div></div>
      <div class="service-tile"><div class="service-tile__art" role="img" aria-label="Piktogramm: Person wirft Abfall in einen Eimer"></div></div>
    </div>
  </section>

</div>
</body>
</html>
```